Easy Re-Design for Hot Chicken and Food Bags

We are a medium sized Deli and Butchery looking to do our own print on our Roast Chicken and Hot Food bags. I am looking for 2 designs:
1 x Roast Chicken Bag
1 x Hot Food Bag for all other hot items
I would like them to look modern and easy to read. Same theme but different so its easy to determine. The less colours used, the better. And only the Roast Chicken Bag needs an ingredients section for the stuffing (to be confirmed) and a barcode.
We attempted the Graphics on this but we are after a professional to make it look as appealing as possible, so we sell as many as possible. : )
Middle Income Families

```html
<!DOCTYPE html>
<html lang="en">
<head>
<meta charset="utf-8">
<title>Grill Yard – Hot Food and Roast Chicken Bags</title>
<link rel="stylesheet" href="https://fonts.googleapis.com/css2?family=Montserrat:wght@400;600;900&family=Oswald:wght@500&display=swap">
<style>
  :root {
    --stage-light: #6f6f72;
    --stage-dark: #5e5e60;
    --charcoal: #363537;
    --banner: #3a393b;
    --white: #ffffff;
    --pattern: #ececec;
    --brand-red: #e8323a;
    --band-red: #e00000;
    --flame-deep: #f07a10;
    --flame-mid: #f9a51c;
    --flame-light: #ffd84a;
  }
  * { box-sizing: border-box; margin: 0; padding: 0; }
  html, body { width: 1018px; height: 1200px; overflow: hidden; }
  body {
    position: relative;
    font-family: "Montserrat", sans-serif;
    background: linear-gradient(to top left, var(--stage-dark) 50%, var(--stage-light) 50%);
  }
  .bag-label {
    position: absolute;
    left: 233px;
    width: 513px;
    height: 430px;
  }
  .bag-label--hot-food { top: 127px; }
  .bag-label--chicken { top: 636px; }

  .top-band { position: absolute; left: 0; top: 0; width: 100%; height: 81px; }
  .top-band--flames {
    background: linear-gradient(to bottom, var(--banner) 0%, var(--flame-deep) 35%, var(--flame-mid) 70%, var(--flame-light) 100%);
  }
  .top-band--chicken {
    background: linear-gradient(to right, var(--band-red), #f03a2e 25%, var(--band-red) 50%, #f03a2e 75%, var(--band-red));
  }
  .pattern-field {
    position: absolute; left: 0; top: 81px; width: 100%; height: 175px;
    background: var(--pattern);
  }
  .flame-field {
    position: absolute; left: 0; top: 248px; width: 100%; height: 89px;
    background: linear-gradient(to bottom, rgba(255,216,74,0) 0%, var(--flame-mid) 35%, var(--flame-deep) 65%, var(--flame-mid) 100%);
  }
  .name-base {
    position: absolute; left: 0; top: 337px; width: 100%; height: 93px;
    background: var(--charcoal);
    clip-path: polygon(0 0, 100% 0, 87.3% 100%, 12.7% 100%);
    display: flex; flex-direction: column; align-items: center; justify-content: center;
  }
  .product-name--hot {
    font-weight: 900; font-size: 60px; letter-spacing: 1px;
    color: var(--flame-mid);
    line-height: 1;
  }
  .product-name--chicken { text-align: left; line-height: 1; }
  .product-name__kicker {
    display: block; font-weight: 400; font-size: 27px; color: var(--white); letter-spacing: 0.3px;
  }
  .product-name__main {
    display: block; font-weight: 900; font-size: 55px; line-height: 50px; color: var(--brand-red); letter-spacing: 0.5px;
  }

  .info-banner {
    position: absolute; left: 181px; top: 0; width: 151px; height: 300px;
    background: linear-gradient(to right, var(--banner) 0%, #4a494b 40%, var(--banner) 70%);
    clip-path: polygon(0 0, 100% 0, 100% 90%, 50% 100%, 0 90%);
    padding: 0 9px;
  }
  .brand-name {
    margin-top: 60px;
    font-family: "Oswald", sans-serif;
    font-weight: 500; font-size: 48px; line-height: 50px;
    color: var(--white); text-align: center;
  }
  .info-banner__rule { margin-top: 8px; height: 1px; background: var(--white); opacity: 0.9; }
  .ingredients__title { margin-top: 11px; margin-left: 5px; font-weight: 600; font-size: 11px; color: var(--white); }
  .ingredients__text {
    margin: 6px 6px 0 5px;
    font-size: 5.9px; line-height: 7.9px; color: #e6e6e6; text-align: justify;
  }
</style>
</head>
<body>

<section class="bag-label bag-label--hot-food" aria-label="Hot food bag">
  <div class="top-band top-band--flames" role="img" aria-label="Row of flames"></div>
  <div class="pattern-field" role="img" aria-label="Repeating brand pattern"></div>
  <div class="flame-field" role="img" aria-label="Row of flames"></div>
  <div class="name-base"><h2 class="product-name--hot">HOT FOOD</h2></div>
  <div class="info-banner">
    <h1 class="brand-name">GRILL<br>YARD</h1>
    <div class="info-banner__rule"></div>
    <h3 class="ingredients__title">Ingredents :</h3>
    <p class="ingredients__text">Lorem ipsum, or lipsum as it is sometimes known, is dummy text used in laying out print, graphic or web designs. The passage is attributed to an unknown typesetter in the 15th century who is thought to have scrambled parts of an old Latin essay on ethics for use in a type specimen book.</p>
  </div>
</section>

<section class="bag-label bag-label--chicken" aria-label="Whole roast chicken bag">
  <div class="top-band top-band--chicken" role="img" aria-label="Row of chicken drumsticks on red"></div>
  <div class="pattern-field" role="img" aria-label="Repeating brand pattern"></div>
  <div class="flame-field" role="img" aria-label="Row of flames"></div>
  <div class="name-base">
    <h2 class="product-name--chicken">
      <span class="product-name__kicker">WHOLE ROAST</span>
      <span class="product-name__main">CHICKEN</span>
    </h2>
  </div>
  <div class="info-banner">
    <h1 class="brand-name">GRILL<br>YARD</h1>
    <div class="info-banner__rule"></div>
    <h3 class="ingredients__title">Ingredents :</h3>
    <p class="ingredients__text">Lorem ipsum, or lipsum as it is sometimes known, is dummy text used in laying out print, graphic or web designs. The passage is attributed to an unknown typesetter in the 15th century who is thought to have scrambled parts of an old Latin essay on ethics for use in a type specimen book.</p>
  </div>
</section>

</body>
</html>
```